Animal Eye Clinic needs a Business card

We are a new veterinary ophthalmology practice (Tessaly Animal Eye Care) and we need a business card designed. We only see animal eyes - we are not a regular veterinary clinic. We already have a logo. We are looking for a professional, good looking business card to hand out to our clients. We are looking for something simple but professional and contemporary. Our logo is likely the only picture/graphic that needs to be on the card.
Updates

Contact Information for Business Card

Marisol Dunkley, BSc, DVM, MSc, DipACVO
Veterinary Ophthalmologist

Phone: 250.418.3097
Email: tessalyanimaleyecare@mailbrook.net
Website: tessalyanimaleyecare.net
Address: 1840 Pellworth Rd
Kelowna, BC, V4T 8M3

Colors

Designer to choose colors to be used in the design.

Requirements
Must have
• Our logo (attached)

```html
<!DOCTYPE html>
<html lang="en">
<head>
<meta charset="utf-8">
<title>Tessaly Animal Eye Care – Business Card</title>
<link rel="stylesheet" href="https://fonts.googleapis.com/css2?family=Archivo:wght@300;700&display=swap">
<style>
  :root {
    --teal: #3aaab5;
    --teal-deep: #2f9aa6;
    --grey: #a9a9a9;
    --grey-text: #8c8c8c;
    --card: #f7f7f7;
    --backdrop: #e9eaea;
  }
  * { margin: 0; padding: 0; box-sizing: border-box; }
  html, body {
    width: 1200px;
    height: 900px;
    overflow: hidden;
    background: var(--backdrop);
  }
  .canvas {
    position: relative;
    width: 1200px;
    height: 900px;
  }
  .business-card {
    position: absolute;
    left: 75px;
    top: 150px;
    width: 1050px;
    height: 600px;
    background: var(--card);
    overflow: hidden;
    box-shadow: 0 12px 40px rgba(0,0,0,0.12);
  }
  .card-shapes {
    position: absolute;
    inset: 0;
    width: 100%;
    height: 100%;
  }
  .shape-teal { fill: var(--teal); }
  .shape-teal-deep { fill: var(--teal-deep); }
  .shape-grey { fill: var(--grey); }
  .practice-name {
    position: absolute;
    left: 130px;
    top: 302px;
    width: 450px;
    font-family: "Archivo", "Helvetica Neue", Arial, sans-serif;
    text-transform: uppercase;
    line-height: 1;
  }
  .practice-name__place {
    display: block;
    font-weight: 300;
    font-size: 26px;
    letter-spacing: 1.62em;
    color: var(--grey-text);
    margin-bottom: 8px;
    white-space: nowrap;
  }
  .practice-name__service {
    display: block;
    font-weight: 700;
    font-size: 45px;
    letter-spacing: 0.01em;
    color: var(--teal-deep);
    white-space: nowrap;
  }
</style>
</head>
<body>
  <main class="canvas">
    <section class="business-card" aria-label="Tessaly Animal Eye Care business card, front">
      <svg class="card-shapes" viewBox="0 0 1050 600" preserveAspectRatio="none" aria-hidden="true">
        <path class="shape-teal" d="M0 0 H190 Q60 110 0 280 Z"/>
        <path class="shape-teal-deep" d="M0 330 Q110 560 430 600 H0 Z"/>
        <circle class="shape-teal" cx="885" cy="290" r="290"/>
        <path class="shape-grey" d="M1050 380 V600 H900 Q990 500 1050 380 Z"/>
      </svg>
      <h1 class="practice-name">
        <span class="practice-name__place">Tessaly</span>
        <span class="practice-name__service">Animal Eye Care</span>
      </h1>
    </section>
  </main>
</body>
</html>
```